contemporary upscale hair salon

we need a business card design for a modern upscale salon. I would like the card to be vertical, simple, and easy to read. I would like a black matte finish on the info side with white on the back of the card, white lettering with a splash of red incorporated somewhere in there. I also want to incorporate embossing and/or cut out in the letters. The info I would like; Name of the business (Vessa Salon) stylist name (Joan) phone number(5093146620) and web address (www.vessasalon-example.com) I am open to putting shears on the card but without it looking too cheap. Looking for something really modern and edgy. these are just ideas I have, but feel free to show me your creative ideas.
please note: the website is still under construction please do not use any images or colors off the web page. Also i currently do not have a logo, that will be a future project.

```html
<!DOCTYPE html>
<html lang="en">
<head>
<meta charset="utf-8">
<title>Vessa Salon – Business Card</title>
<link href="https://fonts.googleapis.com/css2?family=Ubuntu:wght@400;500&display=swap" rel="stylesheet">
<style>
  :root {
    --page-bg: #ffffff;
    --card-bg: #141313;
    --card-edge: #000000;
    --ink: #f4f2f2;
    --accent-red: #e0342a;
  }
  html, body {
    margin: 0;
    padding: 0;
    width: 1200px;
    height: 900px;
    overflow: hidden;
    background: var(--page-bg);
  }
  .canvas {
    position: relative;
    width: 1200px;
    height: 900px;
  }
  .business-card {
    position: absolute;
    left: 352px;
    top: 24px;
    width: 490px;
    height: 858px;
    box-sizing: border-box;
    background: var(--card-bg);
    border: 1px solid var(--card-edge);
    font-family: "Ubuntu", sans-serif;
    color: var(--ink);
    text-align: center;
  }
  .brand {
    position: absolute;
    top: 262px;
    left: 0;
    right: 0;
    display: flex;
    justify-content: center;
    align-items: center;
    gap: 14px;
  }
  .brand-mark {
    width: 22px;
    height: 22px;
    background: var(--accent-red);
  }
  .brand-name {
    margin: 0;
    font-weight: 500;
    font-size: 46px;
    line-height: 1;
    letter-spacing: 3px;
    color: var(--ink);
  }
  .contact {
    position: absolute;
    left: 0;
    right: 0;
    top: 644px;
  }
  .stylist {
    margin: 0;
    font-weight: 400;
    font-size: 42px;
    line-height: 50px;
    letter-spacing: 1px;
  }
  .stylist .role {
    font-size: 30px;
    letter-spacing: 1px;
  }
  .phone {
    margin: 0;
    font-weight: 400;
    font-size: 42px;
    line-height: 50px;
    letter-spacing: 4px;
  }
  .website {
    margin: 8px 0 0;
    font-weight: 400;
    font-size: 29px;
    line-height: 44px;
    letter-spacing: 0.5px;
    color: var(--accent-red);
  }
</style>
</head>
<body>
  <main class="canvas">
    <article class="business-card">
      <header class="brand">
        <span class="brand-mark" aria-hidden="true"></span>
        <h1 class="brand-name">vessa salon</h1>
      </header>
      <section class="contact">
        <p class="stylist">joan <span class="role">(stylist)</span></p>
        <p class="phone">5093146620</p>
        <p class="website">www.vessasalon-example.com</p>
      </section>
    </article>
  </main>
</body>
</html>
```